Marlow Cat Lodge needs a website and a logo :)

I need a web design for my pet hotel. I will use it in Wordpress, probable with Elementor, so if you can also offer the WP template creation, that's a bonus but I don't wanna book the coded-website option here as I don't think that applies to WP. It would be great if you come up with a logo as well.

Here some info:

Modern, premium cat boarding with a vet on-site

Marlow Cat Lodge is a boutique cat boarding facility in Nelson, New Zealand, offering high-quality, vet-supervised care for all cats, including those with special medical needs. Unlike standard catteries, we focus on low-stress boarding, with separate spaces for special-needs and healthy cats, ensuring a safe, comfortable, and peaceful environment. We also prioritize convenience with self check-in and check-out, leveraging technology to enhance the experience.

Target Market(s)

Cat owners for short term to long term stays that don't want the cheapest option and will value that we have a vet on-site

Industry/Entity Type

cat boarding

Number of Pages Required

5+ page

Font styles to use
Sans Serif
Other font styles liked:
• Nothing that needs installation or a license. Please use Google Fonts.

Requirements
Must have
• Landing page, about us, services, blog and contact page - the landing page should have the typical sales layout with hero image top right, a tag line "Modern, premium cat boarding with a vet on-site" and 2 paragraphs. Paragraph 1 (Problem): Leaving your cat behind can be stressful, especially if they need special care. Standard catteries often lack vet oversight and a calm, tailored environment. Paragraph 2 (Solution): At Marlow Cat Lodge, we offer premium, vet-supervised boarding with separate spaces for special-needs and healthy cats. Our self check-in and tech-driven system makes drop-offs and pick-ups effortless... you know the drill :)
Nice to have
• Ask ChatGPT for some ideas and give it the business plan: https://files.example-docs.net/document/d/7qerTy_LKMWBP2hfsx8V304UiLoXyOpqRkZjTnWaBcD/edit?usp=sharing
Should not have
• NO DOGS :)

```html
<!DOCTYPE html>
<html lang="en">
<head>
<meta charset="utf-8">
<title>Marlow Cat Lodge</title>
<link href="https://fonts.googleapis.com/css2?family=Quicksand:wght@500;600;700&family=Josefin+Sans:wght@400;600;700&display=swap" rel="stylesheet">
<style>
:root{
  --orange:#f5821f;
  --orange-soft:#f89a4c;
  --slate:#7b8598;
  --slate-dark:#5d6676;
  --ink:#3f4552;
  --text:#5a606c;
  --mist:#e1e4ea;
  --cream:#f3dcc0;
  --white:#ffffff;
}
*{margin:0;padding:0;box-sizing:border-box}
html,body{width:1200px;height:3932px;overflow:hidden}
body{position:relative;background:var(--white);font-family:"Josefin Sans",sans-serif;color:var(--text)}
.abs{position:absolute}
h1,h2,h3,.heading{font-family:"Quicksand",sans-serif;font-weight:700}
.orange{color:var(--orange)}
.underline{position:absolute;height:3px;width:58px;background:var(--orange);border-radius:2px}
.btn{position:absolute;display:flex;align-items:center;justify-content:center;border-radius:24px;font-family:"Josefin Sans",sans-serif;font-weight:700;font-size:14px;letter-spacing:.5px;color:var(--white);text-transform:uppercase}
.btn-slate{background:var(--slate)}
.btn-orange{background:var(--orange)}
.btn-outline{border:2px solid var(--slate);color:var(--slate);background:transparent;font-size:12.5px}
.photo{position:absolute}

/* hero */
.hero{position:absolute;left:0;top:0;width:1200px;height:760px;background:linear-gradient(90deg,#eef0f4 0%,#f2f3f6 40%,#f4eee8 100%)}
.hero-photo{left:520px;top:0;width:680px;height:760px;background:radial-gradient(ellipse at 55% 45%,#f0a866 0%,#f4c79a 30%,#f1e9e1 65%,#eef0f4 100%)}
.header{left:101px;top:21px;width:1017px;height:89px;background:var(--white);border-radius:45px;box-shadow:0 8px 24px rgba(80,90,110,.12)}
.brand{display:flex;align-items:center;gap:10px;font-family:"Quicksand",sans-serif;font-weight:700;font-size:25px;color:var(--ink)}
.brand .dot{width:26px;height:26px;border-radius:50%;background:var(--orange)}
.nav a{position:absolute;top:57px;font-size:14px;font-weight:600;color:var(--ink);text-decoration:none;letter-spacing:.3px}
.nav a.active{border-bottom:2px solid var(--orange);padding-bottom:4px}
.phone-btn{left:939px;top:46px;width:151px;height:35px;font-size:12.5px;border-radius:18px}
.eyebrow{font-size:15px;font-weight:700;letter-spacing:2px;color:var(--slate-dark);text-transform:uppercase}
.hero-title{left:117px;top:240px;font-size:44px;line-height:46px;color:var(--slate-dark)}
.hero-text{left:118px;top:393px;width:400px;font-size:15px;line-height:21px}

/* problem / solution */
.card-problem{left:124px;top:780px;width:475px;height:284px;background:var(--mist);border-radius:0 0 0 80px}
.card-solution{left:608px;top:780px;width:475px;height:284px;background:var(--orange);border-radius:0 80px 0 0}
.ps-title{position:absolute;top:88px;width:100%;text-align:center;font-size:26px;font-family:"Quicksand",sans-serif;font-weight:700}
.ps-text{position:absolute;top:126px;left:55px;right:55px;text-align:center;font-size:14.5px;line-height:19.5px}
.icon-ring{position:absolute;border-radius:50%;background:var(--white);border:2px dashed #c6ccd6}

/* about */
.about-text{left:614px;width:520px;font-size:19px;line-height:23px;color:var(--text)}

/* services */
.svc-card{position:absolute;top:1846px;width:334px;height:434px;background:var(--white);box-shadow:0 6px 20px rgba(60,70,90,.12)}
.svc-card.featured{background:var(--slate)}
.svc-card .svc-photo{position:absolute;left:0;top:0;width:100%;height:220px}
.svc-card .svc-icon{position:absolute;left:46px;top:188px;width:80px;height:80px;border-radius:50%;background:var(--slate);border:4px solid var(--white)}
.svc-card.featured .svc-icon{background:var(--orange)}
.svc-card h3{position:absolute;left:41px;top:280px;font-family:"Josefin Sans",sans-serif;font-size:15px;font-weight:700;color:var(--ink);letter-spacing:.3px}
.svc-card p{position:absolute;left:41px;top:300px;width:250px;font-size:12.5px;line-height:17px}
.svc-card.featured h3,.svc-card.featured p{color:var(--white)}
.svc-card .btn{left:39px;top:367px;width:165px;height:39px}
.svc-card.featured .btn{border-color:var(--white);color:var(--white)}

/* blog */
.blog-side{position:absolute;left:646px;width:470px;height:200px;background:var(--white);border:1px solid #f1cfd4;border-radius:4px}
.blog-side .blog-photo{position:absolute;left:0;top:0;width:206px;height:100%}
.date{display:inline-flex;align-items:center;gap:5px;background:var(--orange);color:var(--white);font-size:10.5px;font-weight:600;padding:4px 8px 3px;border-radius:2px}
.blog-side .date{position:absolute;left:238px;top:20px}
.blog-side h3{position:absolute;left:238px;top:50px;width:210px;font-family:"Josefin Sans",sans-serif;font-weight:600;font-size:17px;line-height:23px;color:var(--ink)}
.blog-side p{position:absolute;left:238px;top:128px;width:200px;font-size:12px;line-height:18px}

/* contact */
.contact{left:133px;top:2999px;width:945px;height:554px;background:var(--slate);border-radius:120px 0 120px 0}
.contact-inner{left:146px;top:3012px;width:919px;height:528px;border:1.5px solid rgba(255,255,255,.55);border-radius:110px 0 110px 0}
.field{position:absolute;background:var(--white);border:1px solid #cfd4dc;display:flex;align-items:center;gap:12px;padding-left:20px;font-size:14px;color:var(--ink)}
.field svg{flex:none}

/* footer */
.foot-head{font-family:"Josefin Sans",sans-serif;font-weight:700;font-size:15px;letter-spacing:1.5px;color:var(--ink)}
.foot-line{position:absolute;height:1px;width:145px;background:#b7bdc8}
.foot-link{position:absolute;font-size:14.5px;color:var(--ink)}
.social{position:absolute;top:3745px;width:28px;height:28px;border-radius:50%;background:var(--orange)}
.round-icon{position:absolute;width:36px;height:36px;border-radius:50%;background:var(--slate);display:flex;align-items:center;justify-content:center}
</style>
</head>
<body>

<!-- HERO -->
<section class="hero">
  <div class="photo hero-photo" role="img" aria-label="Photo of a ginger cat sleeping on a soft white blanket"></div>
  <svg class="abs" style="left:0;top:0" width="1200" height="770" viewBox="0 0 1200 770">
    <polygon points="0,752 600,640 1200,752 1200,770 0,770" fill="#ffffff"/>
    <polyline points="0,752 600,640 1200,752" fill="none" stroke="#5d6676" stroke-width="3"/>
  </svg>
</section>

<header class="abs header">
  <div class="abs brand" style="left:36px;top:30px"><span class="dot"></span>Marlow Cat Lodge</div>
  <nav class="nav">
    <a class="active" href="#" style="left:369px;top:36px">HOME</a>
    <a href="#" style="left:435px;top:36px">ABOUT US</a>
    <a href="#" style="left:550px;top:36px">SERVICES</a>
    <a href="#" style="left:661px;top:36px">BLOG</a>
    <a href="#" style="left:745px;top:36px">CONTACT</a>
  </nav>
</header>
<div class="btn btn-orange phone-btn">
  <svg width="12" height="12" viewBox="0 0 24 24" style="margin-right:5px"><path fill="#fff" d="M6.6 10.8a15.1 15.1 0 0 0 6.6 6.6l2.2-2.2a1 1 0 0 1 1-.25 11.4 11.4 0 0 0 3.6.6 1 1 0 0 1 1 1V20a1 1 0 0 1-1 1A17 17 0 0 1 3 4a1 1 0 0 1 1-1h3.5a1 1 0 0 1 1 1c0 1.25.2 2.45.6 3.6a1 1 0 0 1-.25 1z"/></svg>(+000) 555 0142
</div>

<div class="abs eyebrow" style="left:121px;top:212px">Marlow Cat Lodge <span style="display:inline-block;width:38px;height:2px;background:var(--orange);vertical-align:middle;margin-left:6px"></span></div>
<h1 class="abs hero-title"><span class="orange">Modern, Premium</span><br>Cat Boarding with<br>a Vet On-Site</h1>
<p class="abs hero-text">Lorem ipsum dolor sit amet, consectetur adipiscing elit, sed do eiusmod tempor incididunt ut labore.</p>
<div class="btn btn-slate" style="left:113px;top:455px;width:183px;height:47px">Learn More ›</div>
<div class="btn btn-orange" style="left:305px;top:455px;width:185px;height:47px">View Services ›</div>

<!-- scroll marker -->
<div class="abs" style="left:562px;top:600px;width:76px;height:76px;border-radius:50%;background:rgba(245,130,31,.35)"></div>
<div class="abs" style="left:572px;top:610px;width:56px;height:56px;border-radius:50%;background:var(--orange)"></div>
<svg class="abs" style="left:588px;top:617px" width="24" height="42" viewBox="0 0 24 42">
  <rect x="5" y="2" width="14" height="22" rx="7" fill="none" stroke="#fff" stroke-width="2"/>
  <line x1="12" y1="7" x2="12" y2="12" stroke="#fff" stroke-width="2"/>
  <polyline points="8,29 12,33 16,29" fill="none" stroke="#fff" stroke-width="2"/>
  <polyline points="8,34 12,38 16,34" fill="none" stroke="#fff" stroke-width="2"/>
</svg>

<!-- PROBLEM / SOLUTION -->
<div class="abs card-problem">
  <h2 class="ps-title" style="color:var(--ink)">Problem</h2>
  <p class="ps-text">Leaving your cat behind can be stressful, especially if they need special care. Standard catteries often lack vet oversight and a calm, tailored environment</p>
</div>
<div class="abs card-solution">
  <h2 class="ps-title" style="color:var(--white)">Solutions</h2>
  <p class="ps-text" style="color:var(--white)">At Marlow Cat Lodge, we offer premium, vet-supervised boarding with separate spaces for special-needs and healthy cats. Our self check-in and tech-driven system makes drop-offs and pick-ups effortless... you know the drill</p>
</div>
<div class="icon-ring" style="left:305px;top:736px;width:104px;height:104px"></div>
<div class="abs" style="left:311px;top:742px;width:92px;height:92px;border-radius:50%;background:var(--slate)"></div>
<div class="icon-ring" style="left:788px;top:742px;width:104px;height:104px"></div>
<div class="abs" style="left:796px;top:750px;width:88px;height:88px;border-radius:50%;background:#fff;border:2px solid #f6d2b3"></div>
<div class="abs" style="left:573px;top:886px;width:60px;height:60px;border-radius:50%;background:#fff;box-shadow:0 3px 10px rgba(0,0,0,.12)"></div>
<div class="abs" style="left:591px;top:904px;width:24px;height:24px;border-radius:50%;background:var(--orange)"></div>

<!-- ABOUT -->
<div class="abs" style="left:69px;top:1112px;width:504px;height:504px;border-radius:50%;background:linear-gradient(135deg,#f0d7b6 0%,#fbf3ea 55%,#f3e2cc 100%)"></div>
<div class="photo" role="img" aria-label="Photo of a person brushing a relaxed ginger cat" style="left:110px;top:1153px;width:422px;height:422px;border-radius:50%;background:radial-gradient(circle at 45% 65%,#e39a5a 0%,#d5a27a 35%,#c9c6cc 70%,#b9bcc6 100%)"></div>

<div class="abs eyebrow" style="left:614px;top:1160px;font-size:15px;font-weight:600;color:var(--slate)">WHO WE ARE</div>
<h2 class="abs" style="left:610px;top:1188px;font-size:44px;line-height:47px;color:var(--slate-dark)"><span class="orange">About Marlow</span><br>Cat Lodge</h2>
<div class="underline" style="left:614px;top:1292px"></div>
<p class="abs about-text" style="top:1316px">Lorem ipsum dolor sit amet, consectetur adipiscing elit, sed do eiusmod tempor incididunt ut labore et dolore magna aliqua. Ut enim ad minim veniam, quis nostrud exercitation ullamco laboris nisi ut aliquip ex ea</p>
<p class="abs about-text" style="top:1434px">Aommodo consequat Duis aute irure dolor in reprehenderit in voluptate velit esse cillum dolore eu</p>
<div class="btn btn-slate" style="left:612px;top:1504px;width:184px;height:47px">Learn More ›</div>

<!-- SERVICES -->
<div class="abs" style="left:0;top:1600px;width:1200px;height:466px;background:linear-gradient(90deg,#f07c22 0%,#f5872c 50%,#f58a30 100%)"></div>
<svg class="abs" style="left:0;top:1596px" width="1200" height="150" viewBox="0 0 1200 150">
  <polygon points="0,0 1200,0 1200,10 600,128 0,10" fill="#ffffff"/>
  <polyline points="0,14 600,134 1200,14" fill="none" stroke="#b3bac7" stroke-width="9"/>
</svg>
<h2 class="abs" style="left:0;top:1752px;width:1200px;text-align:center;font-size:42px;color:var(--white)">Services Provide</h2>
<div class="underline" style="left:579px;top:1813px;background:var(--white)"></div>

<div class="svc-card" style="left:98px">
  <div class="svc-photo" role="img" aria-label="Photo of a tabby cat being gently groomed" style="background:linear-gradient(135deg,#9fb6cc 0%,#c9b39a 55%,#8d7c6a 100%)"></div>
  <div class="svc-icon"></div>
  <h3>SERVICE HEADING</h3>
  <p>Lorem ipsum dolor sit amet, consectetur adipiscing elit, sed do eiusmod tempor incididunt ut labore et</p>
  <div class="btn btn-outline">Learn More ›</div>
</div>
<div class="svc-card featured" style="left:450px">
  <div class="svc-photo" role="img" aria-label="Photo of a vet checking a tabby cat with a stethoscope" style="background:linear-gradient(135deg,#e9ecef 0%,#b89a7c 55%,#dfe2e6 100%)"></div>
  <div class="svc-icon"></div>
  <h3 style="top:284px">SERVICE HEADING</h3>
  <p style="top:304px">Lorem ipsum dolor sit amet, consectetur adipiscing elit, sed do eiusmod tempor incididunt ut labore et dolore magna aliqua.</p>
  <div class="btn btn-outline" style="left:30px;top:370px">Learn More ›</div>
</div>
<div class="svc-card" style="left:802px">
  <div class="svc-photo" role="img" aria-label="Photo of a grey and white cat having its teeth brushed" style="background:linear-gradient(135deg,#d9dde3 0%,#a9abb2 50%,#e7e3e0 100%)"></div>
  <div class="svc-icon"></div>
  <h3>SERVICE HEADING</h3>
  <p>Lorem ipsum dolor sit amet, consectetur adipiscing elit, sed do eiusmod tempor incididunt ut labore et</p>
  <div class="btn btn-outline">Learn More ›</div>
</div>

<!-- BLOGS -->
<div class="abs eyebrow" style="left:120px;top:2367px;font-size:15px;font-weight:600;color:var(--slate)">RESOURCES</div>
<h2 class="abs" style="left:119px;top:2386px;font-size:42px;color:var(--slate-dark)"><span class="orange">Latest</span> Blogs</h2>
<div class="underline" style="left:121px;top:2442px"></div>

<div class="photo" role="img" aria-label="Photo of a fluffy kitten held by a vet in blue gloves" style="left:113px;top:2480px;width:516px;height:417px;background:linear-gradient(160deg,#7f9fc4 0%,#b7bcc6 40%,#8c8f98 70%,#4c5260 100%)"></div>
<div class="abs" style="left:113px;top:2700px;width:516px;height:197px;background:linear-gradient(180deg,rgba(60,66,80,0) 0%,rgba(60,66,80,.75) 100%)"></div>
<div class="abs" style="left:151px;top:2776px"><span class="date">▦ JAN 20, 2024</span></div>
<h3 class="abs" style="left:150px;top:2808px;width:440px;font-family:'Josefin Sans',sans-serif;font-weight:600;font-size:20px;line-height:27px;color:#fff">Lorem ipsum dolor sit amet, consectetur adipiscing elit sed do eiusmod</h3>

<article class="blog-side" style="top:2480px">
  <div class="blog-photo" role="img" aria-label="Photo of a small tabby kitten receiving care" style="background:linear-gradient(135deg,#3d67b0 0%,#b3a79a 50%,#e6e2de 100%)"></div>
  <span class="date">▦ JAN 20, 2024</span>
  <h3>Sed ut perspiciatis unde omnis iste natus error sit voluptatem accusan</h3>
  <p>Lorem ipsum dolor sit amet, consectetur adipiscindo</p>
</article>
<article class="blog-side" style="top:2697px;left:649px">
  <div class="blog-photo" role="img" aria-label="Photo of a tabby kitten held in a person's arms" style="background:linear-gradient(135deg,#2f3640 0%,#7a6f62 50%,#3b4048 100%)"></div>
  <span class="date">▦ JAN 20, 2024</span>
  <h3>Sed ut perspiciatis unde omnis iste natus error sit voluptatem accusan</h3>
  <p>Lorem ipsum dolor sit amet, consectetur adipiscindo</p>
</article>

<!-- CONTACT -->
<div class="abs" style="left:0;top:3432px;width:1200px;height:500px;background:linear-gradient(180deg,#e4e7ed 0%,#eef0f4 40%,#f3f4f7 100%)"></div>
<div class="abs contact"></div>
<div class="abs contact-inner"></div>
<h2 class="abs" style="left:0;top:3050px;width:1212px;text-align:center;font-size:40px;color:#fff">Contact Us</h2>
<div class="underline" style="left:583px;top:3099px"></div>
<div class="abs" style="left:401px;top:3126px;display:flex;align-items:center;gap:8px;font-size:15px;color:#fff">
  <svg width="18" height="18" viewBox="0 0 24 24"><path fill="#fff" d="M6.6 10.8a15.1 15.1 0 0 0 6.6 6.6l2.2-2.2a1 1 0 0 1 1-.25 11.4 11.4 0 0 0 3.6.6 1 1 0 0 1 1 1V20a1 1 0 0 1-1 1A17 17 0 0 1 3 4a1 1 0 0 1 1-1h3.5a1 1 0 0 1 1 1c0 1.25.2 2.45.6 3.6a1 1 0 0 1-.25 1z"/></svg>(+000) 555 0142
</div>
<div class="abs" style="left:607px;top:3126px;display:flex;align-items:center;gap:8px;font-size:15px;color:#fff">
  <svg width="18" height="14" viewBox="0 0 24 18"><rect x="1" y="1" width="22" height="16" rx="2" fill="#fff"/><polyline points="2,2 12,10 22,2" fill="none" stroke="#7b8598" stroke-width="2"/></svg>info@marlowcatlodge.com
</div>

<div class="field" style="left:244px;top:3181px;width:362px;height:53px">
  <svg width="18" height="18" viewBox="0 0 24 24"><circle cx="12" cy="8" r="4.5" fill="none" stroke="#8a92a2" stroke-width="1.6"/><path d="M3.5 21c1-4.5 4.5-6.5 8.5-6.5s7.5 2 8.5 6.5" fill="none" stroke="#8a92a2" stroke-width="1.6"/></svg>First Name*
</div>
<div class="field" style="left:617px;top:3181px;width:362px;height:53px">
  <svg width="18" height="18" viewBox="0 0 24 24"><circle cx="12" cy="8" r="4.5" fill="none" stroke="#8a92a2" stroke-width="1.6"/><path d="M3.5 21c1-4.5 4.5-6.5 8.5-6.5s7.5 2 8.5 6.5" fill="none" stroke="#8a92a2" stroke-width="1.6"/></svg>Last Name*
</div>
<div class="field" style="left:244px;top:3248px;width:362px;height:53px">
  <svg width="20" height="16" viewBox="0 0 24 18"><rect x="1" y="1" width="22" height="16" rx="2" fill="none" stroke="#8a92a2" stroke-width="1.6"/><polyline points="2,2 12,10 22,2" fill="none" stroke="#8a92a2" stroke-width="1.6"/></svg>E-mail*
</div>
<div class="field" style="left:617px;top:3248px;width:362px;height:53px">
  <svg width="18" height="18" viewBox="0 0 24 24"><path fill="none" stroke="#8a92a2" stroke-width="1.6" d="M6.6 10.8a15.1 15.1 0 0 0 6.6 6.6l2.2-2.2a1 1 0 0 1 1-.25 11.4 11.4 0 0 0 3.6.6 1 1 0 0 1 1 1V20a1 1 0 0 1-1 1A17 17 0 0 1 3 4a1 1 0 0 1 1-1h3.5a1 1 0 0 1 1 1c0 1.25.2 2.45.6 3.6a1 1 0 0 1-.25 1z"/></svg>Phone number*
</div>
<div class="field" style="left:244px;top:3314px;width:737px;height:87px;align-items:flex-start;padding-top:14px">
  <svg width="20" height="20" viewBox="0 0 24 24"><path d="M12 3c5 0 9 3.4 9 7.6S17 18.2 12 18.2c-1 0-2-.1-2.9-.4L4 20.5l1.5-4.2C4 14.8 3 12.8 3 10.6 3 6.4 7 3 12 3z" fill="none" stroke="#8a92a2" stroke-width="1.6"/></svg>Leave Message
</div>
<div class="btn btn-orange" style="left:493px;top:3434px;width:223px;height:48px;font-size:15px;letter-spacing:2px">Send Message</div>
<div class="photo" role="img" aria-label="Photo of a grey tabby cat peeking over the form edge" style="left:850px;top:3408px;width:128px;height:172px;border-radius:50% 50% 40% 40%;background:radial-gradient(ellipse at 50% 40%,#c9c9cc 0%,#8f8f95 55%,#6e6f76 100%)"></div>

<!-- FOOTER -->
<div class="abs" style="left:232px;top:3633px;width:34px;height:34px;border-radius:50%;background:var(--orange)"></div>
<div class="abs" style="left:128px;top:3686px;font-family:'Quicksand',sans-serif;font-weight:700;font-size:26px;color:var(--slate-dark)">Marlow Cat Lodge</div>
<div class="social" style="left:151px"></div>
<div class="social" style="left:186px"></div>
<div class="social" style="left:221px"></div>
<div class="social" style="left:256px"></div>
<div class="social" style="left:291px"></div>

<div class="abs foot-head" style="left:408px;top:3638px">NAVIGATION</div>
<div class="foot-line" style="left:408px;top:3662px"></div>
<div class="foot-link" style="left:408px;top:3689px">About us</div>
<div class="foot-link" style="left:408px;top:3715px">Services</div>
<div class="foot-link" style="left:408px;top:3742px">Blogs</div>
<div class="foot-link" style="left:408px;top:3768px">Testimonials</div>

<div class="abs foot-head" style="left:634px;top:3638px">RESOURCES</div>
<div class="foot-line" style="left:634px;top:3662px"></div>
<div class="foot-link" style="left:634px;top:3689px">Faq</div>
<div class="foot-link" style="left:634px;top:3715px">Plans</div>
<div class="foot-link" style="left:634px;top:3742px">Terms of Use</div>
<div class="foot-link" style="left:634px;top:3768px">Contact Us</div>

<div class="abs foot-head" style="left:879px;top:3638px">CONTACT US</div>
<div class="foot-line" style="left:879px;top:3662px"></div>
<div class="round-icon" style="left:878px;top:3694px">
  <svg width="16" height="16" viewBox="0 0 24 24"><path fill="#fff" d="M6.6 10.8a15.1 15.1 0 0 0 6.6 6.6l2.2-2.2a1 1 0 0 1 1-.25 11.4 11.4 0 0 0 3.6.6 1 1 0 0 1 1 1V20a1 1 0 0 1-1 1A17 17 0 0 1 3 4a1 1 0 0 1 1-1h3.5a1 1 0 0 1 1 1c0 1.25.2 2.45.6 3.6a1 1 0 0 1-.25 1z"/></svg>
</div>
<div class="foot-link" style="left:925px;top:3695px;line-height:20px">Phone Number<br><b style="font-weight:600">(+000) 555 0178</b></div>
<div class="round-icon" style="left:878px;top:3752px">
  <svg width="16" height="12" viewBox="0 0 24 18"><rect x="1" y="1" width="22" height="16" rx="2" fill="#fff"/><polyline points="2,2 12,10 22,2" fill="none" stroke="#7b8598" stroke-width="2"/></svg>
</div>
<div class="foot-link" style="left:925px;top:3760px">info@marlowcat.com</div>

<div class="abs" style="left:145px;top:3849px;width:944px;height:1px;background:#c3c8d1"></div>
<div class="abs" style="left:0;top:3879px;width:1200px;text-align:center;font-size:14px;color:var(--ink)">Copyright © 2025 Marlow Cat Lodge All Right Reserved</div>

</body>
</html>
```